Residential improvers, Verdant Lane Homes *

Cozy Perch 2 Go is a real estate company specializing in turning unloved properties into improved, happy places to live. We specialize in thoughtfully-improved residential properties for buyers or renters. Our company needs a business card that reflects the renovated homes we create using green and Feng Shui principles,

Please disregard the images we submitted. We are looking for an abstract, sophisticated elegant design. No eggs in a nest ... nothing cute. The image can be soft.
Updates

Aloha (hello) all designers. We are a serious property investment/improvement company. We strive to be unique, renovating with style and elegance. Our business card must portray the same message. We thought the nest and flower might be "it" ... clearly it's not, once we saw what you submitted. Please revisit the brief as it was modified yesterday. Mahalo for your input! We look forward to hearing from all designers that have been invited.

Industry/Entity Type

Real Estate Development

Contact Information for Business Card

We will have separate business cards for
1) Corabeth Lindqvist 808-555-0173 corabeth@mailbrook.test
2) Marla Fenwright 808-555-0198 marlafenwright@mailbrook.test
** can we add the website later ... in the process of approval.
Acquirers * Restorers * Advisors

Font styles to use
Sans Serif

Colors
cadf82

Requirements
Must have
• a feng shui feel ... modern. Color - green with black print.
Nice to have
• Verdant Lane Homes

```html
<!DOCTYPE html>
<html lang="en">
<head>
<meta charset="UTF-8">
<title>Verdant Lane Homes – Business Card</title>
<link rel="stylesheet" href="https://fonts.googleapis.com/css2?family=Montserrat:wght@400;500;600;700&display=swap">
<style>
  :root {
    --backdrop: #2b2b2d;
    --card-white: #ffffff;
    --brand-green: #cadf82;
    --ink: #141414;
    --ink-soft: #2a2a2a;
  }
  * { margin: 0; padding: 0; box-sizing: border-box; }
  html, body {
    width: 1200px;
    height: 880px;
    overflow: hidden;
    background: var(--backdrop);
    font-family: "Montserrat", Arial, sans-serif;
    color: var(--ink);
  }
  .stage {
    position: relative;
    width: 1200px;
    height: 880px;
  }
  .card {
    position: absolute;
    left: 300px;
    width: 600px;
    height: 343px;
    background: var(--card-white);
    border-radius: 18px;
    overflow: hidden;
  }
  .card--front { top: 80px; }
  .card--back  { top: 457px; }

  .brand {
    position: absolute;
    display: flex;
    align-items: center;
    gap: 12px;
  }
  .brand__dot {
    width: 14px;
    height: 14px;
    border-radius: 50%;
    background: var(--brand-green);
    flex: none;
  }
  .brand__name {
    font-weight: 600;
    color: var(--ink);
    white-space: nowrap;
  }
  .card--front .brand {
    left: 0; right: 0; top: 152px;
    justify-content: center;
  }
  .card--front .brand__name { font-size: 30px; }

  .card--back .brand { left: 40px; top: 112px; }
  .card--back .brand__name { font-size: 26px; }

  .card__art {
    position: absolute;
    inset: 0;
    width: 600px;
    height: 343px;
  }

  .tagline {
    position: absolute;
    right: 28px;
    top: 26px;
    list-style: none;
    text-align: right;
    font-size: 12px;
    font-weight: 500;
    line-height: 1.35;
    color: var(--ink-soft);
  }
  .tagline li::after {
    content: "";
    display: inline-block;
    width: 7px;
    height: 7px;
    margin-left: 7px;
    border-radius: 50%;
    background: var(--brand-green);
    vertical-align: 1px;
  }

  .contact {
    position: absolute;
    right: 26px;
    top: 182px;
    text-align: right;
    font-style: normal;
    color: var(--ink);
  }
  .contact__name {
    font-size: 16px;
    font-weight: 700;
    margin-bottom: 4px;
    margin-right: 24px;
  }
  .contact__line {
    display: flex;
    justify-content: flex-end;
    align-items: center;
    gap: 8px;
    font-size: 12.5px;
    font-weight: 500;
    line-height: 1.55;
  }
  .contact__icon {
    width: 16px;
    height: 16px;
    flex: none;
  }
</style>
</head>
<body>
<main class="stage">

  <section class="card card--front" aria-label="Business card front">
    <div class="brand">
      <span class="brand__dot"></span>
      <span class="brand__name">Verdant Lane Homes</span>
    </div>
  </section>

  <section class="card card--back" aria-label="Business card back">
    <svg class="card__art" viewBox="0 0 600 343" aria-hidden="true">
      <path d="M600 95 C 470 110 430 200 385 255 C 335 318 260 335 150 343 L600 343 Z" fill="var(--brand-green)"/>
      <path d="M590 88 C 440 110 400 210 350 265 C 300 318 230 335 130 343" fill="none" stroke="var(--card-white)" stroke-width="5"/>
      <path d="M598 78 C 430 100 395 205 340 262 C 290 314 215 333 120 343" fill="none" stroke="var(--brand-green)" stroke-width="4"/>
      <path d="M0 292 C 130 312 270 290 300 168 C 296 262 190 318 0 314 Z" fill="var(--ink)"/>
      <path d="M0 322 C 150 330 240 318 290 300 C 250 330 200 343 160 343 L0 343 Z" fill="var(--brand-green)"/>
    </svg>

    <div class="brand">
      <span class="brand__dot"></span>
      <span class="brand__name">Verdant Lane Homes</span>
    </div>

    <ul class="tagline">
      <li>Acquirers</li>
      <li>Restorers</li>
      <li>Advisors</li>
    </ul>

    <address class="contact">
      <p class="contact__name">Corabeth Lindqvist</p>
      <p class="contact__line">808-555-0173
        <svg class="contact__icon" viewBox="0 0 16 16"><circle cx="8" cy="8" r="7" fill="none" stroke="var(--ink)" stroke-width="1.2"/><rect x="5.5" y="3.5" width="5" height="9" rx="1" fill="none" stroke="var(--ink)" stroke-width="1.1"/></svg>
      </p>
      <p class="contact__line">corabeth@mailbrook.test
        <svg class="contact__icon" viewBox="0 0 16 16"><circle cx="8" cy="8" r="7" fill="var(--ink)"/><rect x="4" y="5" width="8" height="6" fill="none" stroke="var(--brand-green)" stroke-width="1"/><path d="M4 5 L8 8.5 L12 5" fill="none" stroke="var(--brand-green)" stroke-width="1"/></svg>
      </p>
      <p class="contact__line">www.verdantlanehomes.test
        <svg class="contact__icon" viewBox="0 0 16 16"><circle cx="8" cy="8" r="7" fill="var(--ink)"/><circle cx="8" cy="8" r="4" fill="none" stroke="var(--brand-green)" stroke-width="1"/><path d="M4 8 H12 M8 4 V12" stroke="var(--brand-green)" stroke-width="1"/></svg>
      </p>
    </address>
  </section>

</main>
</body>
</html>
```